Fitness competition business needs a card design

I need a professional business card design using my logo. The card will be horizontal with rounded edges.

Target Market(s)

Female fitness competitors

Industry/Entity Type

Fitness

Contact Information for Business Card

Lise-Anne Korvath
Owner
stagevelora.com
210.555.0137
info@stagevelora.com

Font styles to use
Serif

Colors

Designer to choose colors to be used in the design.

Requirements
Must have
• On the back please add the following:
• Figure
• Bikini
• Physique
• Fitness
Nice to have
• Looking for a very sleek design, contemporary and easy to read.
Should not have
• Should not be difficult to read or be too busy

```html
<!DOCTYPE html>
<html lang="en">
<head>
<meta charset="utf-8">
<title>Stage Velora – Business Card</title>
<link rel="stylesheet" href="https://fonts.googleapis.com/css2?family=Source+Serif+4:wght@400;700&display=swap">
<style>
  :root {
    --brand-red: #e8232a;
    --brand-grey: #57585a;
    --paper: #ffffff;
    --backdrop: #ecebe8;
  }
  html, body {
    margin: 0;
    padding: 0;
    width: 1200px;
    height: 900px;
    overflow: hidden;
    background: var(--backdrop);
    font-family: "Source Serif 4", Georgia, serif;
  }
  .canvas {
    position: relative;
    width: 1200px;
    height: 900px;
  }
  .card {
    position: absolute;
    box-shadow: 0 4px 14px rgba(0,0,0,0.18);
    overflow: hidden;
  }

  /* Front */
  .card-front {
    left: 177px; top: 73px;
    width: 588px; height: 364px;
    background: var(--brand-grey);
    color: var(--paper);
  }
  .front-band {
    position: absolute;
    left: 0; top: 0;
    width: 68px; height: 100%;
    background: var(--brand-red);
  }
  .front-emblem {
    position: absolute;
    left: 20px; top: 88px;
    width: 176px; height: 176px;
    border-radius: 50%;
    background: var(--paper);
    display: flex;
    align-items: center;
    justify-content: center;
  }
  .front-emblem .brand-name {
    color: var(--brand-red);
    font-weight: 700;
    font-size: 17px;
    letter-spacing: 0.5px;
  }
  .holder-name {
    position: absolute;
    right: 41px; top: 74px;
    margin: 0;
    font-size: 20px;
    font-weight: 700;
    letter-spacing: 0.3px;
    line-height: 24px;
  }
  .contact-list {
    position: absolute;
    right: 36px; top: 190px;
    margin: 0; padding: 0;
    list-style: none;
    text-align: right;
    font-size: 16px;
    line-height: 22.5px;
  }
  .contact-list li {
    display: flex;
    justify-content: flex-end;
    align-items: center;
    gap: 5px;
  }
  .contact-list svg { width: 13px; height: 13px; fill: var(--paper); }
  .address {
    position: absolute;
    right: 36px; top: 276px;
    margin: 0;
    font-style: normal;
    text-align: right;
    font-size: 16px;
    line-height: 21px;
  }

  /* Back */
  .card-back {
    left: 388px; top: 507px;
    width: 567px; height: 350px;
    background: var(--paper);
  }
  .rule { position: absolute; left: 0; width: 100%; }
  .rule-top-thick { top: 0; height: 7px; background: var(--brand-grey); }
  .rule-top-thin { top: 11px; height: 3px; background: var(--brand-grey); }
  .rule-bottom-thin { bottom: 15px; height: 3px; background: var(--brand-red); }
  .rule-bottom-thick { bottom: 0; height: 10px; background: var(--brand-red); }
  .back-brand {
    position: absolute;
    left: 0; top: 100px;
    width: 100%;
    display: flex;
    flex-direction: column;
    align-items: center;
  }
  .back-brand .brand-dot {
    width: 54px; height: 54px;
    border-radius: 50%;
    background: var(--brand-grey);
    margin-bottom: 14px;
  }
  .back-brand .brand-name {
    color: var(--brand-red);
    font-weight: 700;
    font-size: 30px;
    line-height: 36px;
    letter-spacing: 1px;
  }
  .back-brand .divisions {
    margin: 18px 0 0;
    padding: 0;
    list-style: none;
    display: flex;
    gap: 12px;
    color: var(--brand-grey);
    font-size: 14px;
    letter-spacing: 2px;
  }
  .divisions li + li::before {
    content: "·";
    margin-right: 12px;
    color: var(--brand-red);
  }
</style>
</head>
<body>
<main class="canvas">

  <section class="card card-front" aria-label="Card front">
    <div class="front-band"></div>
    <div class="front-emblem"><span class="brand-name">STAGE VELORA</span></div>
    <h1 class="holder-name">LISE-ANNE KORVATH</h1>
    <ul class="contact-list">
      <li>210.555.0137
        <svg viewBox="0 0 16 16" aria-hidden="true"><path d="M2 6c0-2 3-3 6-3s6 1 6 3v1h-3V6H5v1H2zM4 8h8l2 5H2z"/></svg>
      </li>
      <li>info@stagevelora.com
        <svg viewBox="0 0 16 16" aria-hidden="true"><path d="M1 3h14v10H1zM2 4l6 5 6-5v-.1H2z" fill-rule="evenodd"/></svg>
      </li>
      <li>stagevelora.com
        <svg viewBox="0 0 16 16" aria-hidden="true"><circle cx="8" cy="8" r="7"/></svg>
      </li>
    </ul>
    <address class="address">421, Marlow Avenue<br>San Antonio, 78205</address>
  </section>

  <section class="card card-back" aria-label="Card back">
    <div class="rule rule-top-thick"></div>
    <div class="rule rule-top-thin"></div>
    <div class="back-brand">
      <span class="brand-dot"></span>
      <span class="brand-name">STAGE VELORA</span>
      <ul class="divisions">
        <li>FIGURE</li>
        <li>BIKINI</li>
        <li>PHYSIQUE</li>
        <li>FITNESS</li>
      </ul>
    </div>
    <div class="rule rule-bottom-thin"></div>
    <div class="rule rule-bottom-thick"></div>
  </section>

</main>
</body>
</html>
```